Vexaroll needs a newsletter to introduce our new test - Helix Body Balance

I need a newsletter or email design to introduce a new test that my company has to offer called Helix Body Balance. We are launching this genetic test to fitness centers, nutritionists, high end gyms, personal trainers and others. The genetic test looks at 5 genetic markers that are key to how each individual processes nutrients, carbohydrates etc and then provides a comprehensive report for the individual on specific diet plans, exercise regimens and their genetic results. The newsletter should be an exciting announcement of this new test and one that can easily be used via email or via attachments. I have attached some files which provide much more detail. The final design should communicate an opportunity for these potential customers to increase revenue, provide their members with an extraordinary personalized genetic test and to provide a value add to their current offerings.
Updates
Hi,
I forgot to upload a one page marketing piece that i had created as well as the logo for vexaroll. Happy to provide just not sure how to upload them into the project
Target Market(s)
fitness centers, high end gyms, nutritionists, dieticians, personal trainers, health coaches
Colors
Designer to choose colors to be used in the design.
Look and feel
Each slider illustrates characteristics of the customer's brand and the style your logo design should communicate.

```html
<!DOCTYPE html>
<html lang="en">
<head>
<meta charset="utf-8">
<title>Vexaroll – New Helix Body Balance Test</title>
<link rel="stylesheet" href="https://fonts.googleapis.com/css2?family=Bebas+Neue&family=Tinos:wght@400;700&display=swap">
<style>
  :root {
    --paper: #e1e9f0;
    --navy: #0f2366;
    --teal: #4ccfc6;
    --photo-light: #2f7fb8;
    --photo-dark: #0b2c4c;
  }
  html, body {
    margin: 0;
    padding: 0;
    width: 1200px;
    height: 2400px;
    overflow: hidden;
    background: var(--paper);
  }
  .newsletter {
    position: relative;
    width: 1200px;
    height: 2400px;
    background: var(--paper);
    font-family: "Tinos", "Times New Roman", serif;
    color: var(--navy);
  }
  .headline-new {
    position: absolute;
    left: 112px;
    top: 62px;
    margin: 0;
    font-family: "Bebas Neue", "Oswald", sans-serif;
    font-weight: 400;
    font-size: 290px;
    line-height: 1;
    letter-spacing: 2px;
    color: var(--navy);
    transform: skewX(-12deg);
  }
  .brand {
    position: absolute;
    left: 870px;
    top: 200px;
    width: 240px;
    text-align: center;
    font-family: "Tinos", "Times New Roman", serif;
    font-size: 38px;
    color: var(--navy);
  }
  .product-title {
    position: absolute;
    left: 118px;
    top: 330px;
    margin: 0;
    font-family: "Bebas Neue", "Oswald", sans-serif;
    font-weight: 400;
    font-size: 118px;
    line-height: 104px;
    letter-spacing: 5px;
    color: var(--teal);
  }
  .tagline {
    position: absolute;
    left: 120px;
    top: 572px;
    margin: 0;
    font-family: "Bebas Neue", "Oswald", sans-serif;
    font-weight: 400;
    font-size: 60px;
    letter-spacing: 2px;
    color: var(--navy);
    transform: skewX(-12deg);
  }
  .hero-visual {
    position: absolute;
    left: 108px;
    top: 670px;
    width: 984px;
    height: 576px;
    background: radial-gradient(ellipse at 48% 55%, var(--photo-light) 0%, #1a5688 45%, var(--photo-dark) 100%);
  }
  .section-bar {
    position: absolute;
    left: 108px;
    top: 1286px;
    width: 978px;
    height: 88px;
    background: var(--navy);
  }
  .section-bar h2 {
    margin: 0;
    padding-left: 12px;
    font-family: "Bebas Neue", "Oswald", sans-serif;
    font-weight: 400;
    font-size: 70px;
    line-height: 92px;
    letter-spacing: 2px;
    color: var(--teal);
  }
  .about-copy {
    position: absolute;
    left: 120px;
    top: 1392px;
    width: 960px;
    font-size: 31px;
    line-height: 45px;
    color: var(--navy);
  }
  .about-copy p { margin: 0 0 46px; }
  .about-copy .visit { text-align: center; margin-top: 58px; }
  .call-to-action {
    position: absolute;
    left: 0;
    top: 2108px;
    width: 1200px;
    margin: 0;
    text-align: center;
    font-family: "Bebas Neue", "Oswald", sans-serif;
    font-weight: 400;
    font-size: 50px;
    line-height: 52px;
    letter-spacing: 3px;
    color: var(--teal);
  }
</style>
</head>
<body>
<main class="newsletter">
  <h1 class="headline-new">New</h1>
  <div class="brand">Vexaroll</div>
  <h2 class="product-title">Helix Body Balance<br>Test</h2>
  <p class="tagline">Say goodbye to one-size fits all dieting</p>

  <div class="hero-visual" role="img" aria-label="Glowing DNA double helix held between fingertips on a deep blue background"></div>

  <div class="section-bar"><h2>About Us</h2></div>

  <div class="about-copy">
    <p>Vexaroll is proud to offer a line of genetic tests that allow wellness minded individuals to <strong>discover</strong> their genetic makeup as it pertains to weight management.</p>
    <p>The genetic test looks at 5 genetic markers that are key to how each individual processes nutrients, carbohydrates etc and then provides a comprehensive report for the individual on specific diet plans, exercise regimens and their genetic results.</p>
    <p class="visit">Visit <strong>www.vexaroll.com</strong> to learn more about us, our services, the testing that we offer and the amazing reports that we provide</p>
  </div>

  <p class="call-to-action">Let us help your members<br>personalize a diet &amp; exercise ratio<br>that fits them based on their genetic makeup!</p>
</main>
</body>
</html>
```